Webdesign für visa-korvenet.org
Kreativer Initialvorschlag, schnelle Umsetzung, flexible Anpassung des Designvorschlags und nette Kommunikation, gerne wieder!
Zielgruppe
Wir vermitteln weltweit Reisegenehmigungen für Geschäfts- und Privatkunden. Auf VISA-Korvenet.org möchten wir auf deutsch, englisch & chinesisch Reisenden bei der Beiholung von Kurzzeit, Work & Travel & diversen Visaarten helfen.
Aufgabenstellung
Der Webseitezweck ist es, dass Besucher bestellen. Dafür muss die Seite attraktiv, einfach bedienbar und das CTA Element "zum Formular" präsent und mehrfach auftauchen.

```html
<!DOCTYPE html>
<html lang="de">
<head>
<meta charset="utf-8">
<title>VISA-Korvenet.org – Evisitor Visa Australia</title>
<link href="https://fonts.googleapis.com/css2?family=Lato:ital,wght@0,300;0,400;0,700;0,900;1,400&family=Kaushan+Script&display=swap" rel="stylesheet">
<style>
:root{
  --dark:#2e3035;
  --dark-2:#26282c;
  --blue:#3d8fd1;
  --yellow:#f7b233;
  --grey-bg:#ececec;
  --text:#555;
  --text-light:#888;
  --white:#fff;
  --green:#8bc53f;
}
*{box-sizing:border-box;margin:0;padding:0}
html,body{width:1200px;height:4839px;overflow:hidden}
body{font-family:"Lato",sans-serif;color:var(--text);background:var(--white);position:relative}
section,header,footer{position:relative;width:1200px}

/* header */
.site-header{height:131px;background:var(--dark)}
.brand{position:absolute;left:101px;top:54px;color:var(--white)}
.brand-name{font-size:26px;font-weight:900;letter-spacing:-.5px;display:flex;align-items:center;gap:8px}
.brand-name .dot{width:12px;height:12px;background:var(--yellow);border-radius:50%}
.brand-sub{font-size:8px;letter-spacing:.5px;color:#ccc;margin-top:2px}
.topline{position:absolute;top:18px;left:381px;font-size:10px;color:#8a8d93;display:flex;gap:20px}
.toplinks{position:absolute;top:20px;right:100px;font-size:8px;color:#8a8d93;letter-spacing:.4px}
.main-nav{position:absolute;top:80px;left:384px;display:flex;gap:56px;font-size:13px;color:var(--white);letter-spacing:.4px}
.main-nav .active{color:var(--yellow)}
.lang{position:absolute;top:68px;left:1020px;width:78px;height:40px;border:1px solid #aaa;color:var(--white);font-size:13px;display:flex;align-items:center;justify-content:center;gap:6px}

/* hero */
.hero{height:583px;overflow:hidden}
.hero-photo{position:absolute;inset:0;background:linear-gradient(180deg,#7fb3c9 0%,#a8c9d2 25%,#3c8fa3 45%,#6bb4bc 60%,#e2d5c0 80%,#d8c7ad 100%)}
.hero-title{position:absolute;top:165px;width:100%;text-align:center;color:var(--white)}
.hero-title .l1{font-size:88px;font-weight:300;letter-spacing:6px;line-height:1}
.hero-title .l2{font-family:"Kaushan Script",cursive;font-size:110px;line-height:1;margin-top:-10px}
.dots{position:absolute;top:538px;left:572px;display:flex;gap:6px}
.dots span{width:13px;height:13px;border-radius:50%;background:#ddd}
.dots span:first-child{background:var(--dark)}
.social{position:absolute;left:0;top:357px;display:flex;flex-direction:column;gap:2px}
.social span{width:40px;height:38px;background:var(--white);display:flex;align-items:center;justify-content:center}
.social span i{width:12px;height:12px;background:var(--dark);border-radius:50%}

/* cta band */
.cta-band{height:88px;background:var(--yellow);color:var(--white)}
.cta-band p{position:absolute;left:101px;top:33px;font-size:16px}
.cta-band p b{font-weight:700;margin-right:18px}
.cta-band p span{font-weight:300}
.btn{display:inline-flex;align-items:center;justify-content:center;background:var(--white);color:var(--dark);font-weight:700;font-size:17px;letter-spacing:.2px}
.cta-band .btn{position:absolute;left:860px;top:24px;width:238px;height:38px}

/* intro */
.intro{height:385px;text-align:center}
.intro h1{padding-top:68px;font-size:34px;font-weight:700;color:#3a3c40;letter-spacing:-.5px}
.intro .sub{font-size:15px;margin-top:6px}
.intro p.txt{width:800px;margin:30px auto 0;font-size:13px;line-height:23px;color:#666}
.intro p.txt + p.txt{margin-top:20px}

/* cards */
.products{height:669px;background:var(--grey-bg)}
.card{position:absolute;top:55px;width:304px;height:558px;background:var(--dark);color:var(--white);text-align:center;padding:0 30px}
.card.tourist{background:var(--blue)}
.card h2{margin-top:44px;font-size:35px;line-height:40px;letter-spacing:2px;font-weight:300}
.card h2 b{font-weight:900}
.card p{font-size:11.5px;line-height:19px;margin-top:40px;color:#e6e6e6}
.card p.note{margin-top:22px;font-style:italic}
.card .btn{position:absolute;left:33px;bottom:56px;width:238px;height:38px}
.card.tourist .btn{color:var(--blue)}

/* faq */
.faq{height:673px;padding:0 101px}
.faq h2{padding-top:62px;text-align:center;font-size:34px;font-weight:900;color:#3a3c40}
.faq .sub{text-align:center;font-size:15px;margin-top:4px}
.faq-q{height:38px;background:var(--blue);color:var(--white);font-weight:700;font-size:16px;display:flex;align-items:center;justify-content:space-between;padding:0 22px;margin-top:28px}
.faq-q + .faq-q{margin-top:7px}
.faq-q .ico{font-size:30px;font-weight:300;line-height:1}
.faq-a{font-size:15px;line-height:23px;color:#666;padding:14px 0 16px}
.faq-a ul{margin:20px 0 20px 38px;font-size:15px}
.faq-first{margin-top:40px}
.faq-a + .faq-q{margin-top:12px}

/* tips */
.tips{height:544px;color:var(--white);text-align:center;overflow:hidden}
.tips-photo{position:absolute;inset:0;background:linear-gradient(180deg,#5c7d9a 0%,#3f5a74 45%,#2a3d55 75%,#1f2f44 100%)}
.tips h2{position:relative;padding-top:54px;font-size:34px;font-weight:900}
.tips .sub{position:relative;font-size:16px;margin-top:2px}
.tip{position:absolute;top:165px;width:300px;text-align:center}
.tip .num{width:56px;height:56px;border-radius:50%;background:var(--white);color:var(--dark);font-size:30px;font-weight:300;display:flex;align-items:center;justify-content:center;margin:0 auto}
.tip h3{font-size:17px;font-weight:400;letter-spacing:1.5px;line-height:22px;margin-top:14px}
.tip p{font-size:11.5px;font-style:italic;line-height:19px;margin-top:28px;color:#eef}

/* advantages */
.advantages{height:712px;text-align:center}
.advantages h2{padding-top:58px;font-size:34px;font-weight:900;color:#3a3c40}
.advantages .sub{font-size:15px;margin-top:4px}
.compare{position:absolute;left:101px;top:173px;width:998px;border-collapse:collapse;font-size:12px;text-align:left}
.compare td,.compare th{height:33px;padding:0 10px;border-bottom:1px solid #d8d8d8}
.compare th{font-weight:700;color:#333;height:32px}
.compare tr:nth-child(even) td:first-child{background:#f3f3f3}
.compare .col-own{width:140px;background:var(--dark);color:#ccc;text-align:center;border-bottom-color:#3d4046}
.compare .col-gov{width:144px;background:var(--blue);color:#e8f0ff;text-align:center;border-bottom-color:#5aa0da}
.compare th.col-own,.compare th.col-gov{font-weight:400;font-size:11px}
.compare svg{vertical-align:middle}

/* destinations */
.places{height:564px;display:grid;grid-template-columns:355px 282px 281px 282px;grid-template-rows:282px 282px}
.tile{position:relative;display:flex;align-items:flex-start;justify-content:center;color:var(--white);text-align:center}
.tile span{margin-top:112px;font-size:32px;line-height:38px;font-weight:300;letter-spacing:1px}
.tile span b{font-weight:900;display:block}
.visit{grid-row:1 / span 2;background:linear-gradient(160deg,#1f5d7a,#2f8fae 50%,#0f3c52);justify-content:flex-start}
.visit span{margin:180px 0 0 36px;text-align:left;font-size:68px;line-height:80px;letter-spacing:2px}
.sydney{background:linear-gradient(180deg,#e6b680,#cfa070 50%,#4d6d87)}
.perth{background:linear-gradient(180deg,#6f9dc7,#4f7aa0 55%,#2b4561)}
.brisbane{background:linear-gradient(180deg,#8fb1d4,#5e86ad 60%,#36597c)}
.melbourne{background:linear-gradient(180deg,#b0c7de,#7a98b6 55%,#3d5670)}
.tasmania{background:linear-gradient(180deg,#6e7f95,#b0563e 60%,#7a2f22)}
.goldcoast{background:linear-gradient(180deg,#a9d1ea,#6eb4d6 55%,#3f8fb8)}

/* footer */
.site-footer{height:432px;background:var(--dark);color:#ddd;font-size:13px}
.fcol{position:absolute;top:60px}
.fcol h4{font-size:18px;font-weight:700;color:var(--white);margin-bottom:32px}
.fcol p{line-height:23px}
.contact{left:101px;width:260px}
.contact .row{display:flex;gap:20px;margin-top:20px;line-height:23px}
.contact .row svg{flex:none;margin-top:4px}
.links{left:432px}
.links a{display:block;color:#ddd;text-decoration:none;font-size:13px;line-height:35px;margin-top:-8px}
.links a+a{margin-top:0}
.mailing{left:772px;width:330px}
.mail-form{display:flex;margin-top:22px}
.mail-form span{width:210px;height:32px;background:#4a4d53;color:#ccc;font-size:12px;padding:8px 12px}
.mail-form b{width:64px;height:32px;background:var(--yellow);color:var(--white);font-weight:400;display:flex;align-items:center;justify-content:center;font-size:12px}
.mailing h4.pay{margin-top:58px;margin-bottom:24px}
.cards-row{display:flex;gap:12px}
.cards-row span{height:22px;padding:0 10px;background:var(--white);color:var(--dark);font-size:10px;font-weight:700;display:flex;align-items:center}
.copyright{height:58px;background:var(--dark-2);color:#aaa;font-size:12px;padding:22px 101px}
</style>
</head>
<body>

<header class="site-header">
  <div class="brand">
    <div class="brand-name">VISA Korvenet <span class="dot"></span></div>
    <div class="brand-sub">DEUTSCHES FORMULAR · VISA AUSTRALIA</div>
  </div>
  <div class="topline"><span>Unsere Servicehotline (Mo-Fr 10-16 Uhr)</span><span>☎ 0800 100 200 300 (kostenfrei)</span></div>
  <div class="toplinks">IMPRESSUM | DATENSCHUTZ | FAQ | AGB</div>
  <nav class="main-nav">
    <span class="active">START</span><span>TOURISTEN VISUM</span><span>BUSINESS VISUM</span><span>ÜBER ETA</span><span>KONTAKT</span>
  </nav>
  <div class="lang">
    <svg width="16" height="16" viewBox="0 0 16 16"><circle cx="8" cy="8" r="7" fill="none" stroke="#fff" stroke-width="1.5"/><path d="M1 8h14M8 1c3 3 3 11 0 14M8 1c-3 3-3 11 0 14" fill="none" stroke="#fff" stroke-width="1.2"/></svg>DE
  </div>
</header>

<section class="hero">
  <div class="hero-photo" role="img" aria-label="Photo of a kangaroo on a white sand beach with turquoise sea and rocky hills"></div>
  <div class="hero-title"><div class="l1">EXPLORE</div><div class="l2">Australia</div></div>
  <div class="social" aria-label="Social media links"><span><i></i></span><span><i></i></span><span><i></i></span></div>
  <div class="dots"><span></span><span></span><span></span></div>
</section>

<section class="cta-band">
  <p><b>YOU NEED A VISA FOR AUSTRALIA?</b><span>WE'LL GET YOU ONE!</span></p>
  <span class="btn">APPLICATION FORM</span>
</section>

<section class="intro">
  <h1>Evisitor Visa Australia</h1>
  <p class="sub">(former ETA – Electronic Travel Authority Australia)</p>
  <p class="txt">Touristen und Geschäftsleute benötigen zur Einreise nach Australien vor Reisebeginn ein gültiges Visum, kurz „eVisitor“.<br>Bis 2008 hieß dieses Visum noch (Electronic Travel Authority).</p>
  <p class="txt">Eine Evisitor Registrierung ist wie ein Visum zeitlich begrenzt. Sowohl Touristen wie auch Geschäftsreisende können sich mit einem gültigen Evisitor Visum 3 Monate in Australien aufhalten. Evisitor Visa haben eine Gültigkeit von 12 Monaten, somit können Reisende innerhalb eines Jahres auch mehrfach nach Australien einreisen.</p>
</section>

<section class="products">
  <article class="card business" style="left:101px">
    <h2>EVISITOR<br><b>BUSINESS ETA</b></h2>
    <p>Geschäftsreisende benötigen ein Business eVisitor Visum. Dieses ebenso elektronisch erstellte Visum hat eine <b>Gültigkeit von 12 Monaten</b> und kann für einen durchgängigen Geschäftsaufenthalt für bis zu <b>drei Monaten</b> genutzt werden. Wir empfehlen auch bei Messebesuchen ein Business Visum zu beantragen um eine problemlose Einreise zu gewährleisten.</p>
    <p class="note">Wichtig: Es muss bereits vor Antritt der Reise ein gültiges Business Visum vorliegen. Drucken Sie Ihre eVisitor Nummer aus und legen Sie diese Ihren Reisedokumenten bei.</p>
    <span class="btn">APPLICATION FORM</span>
  </article>
  <article class="card tourist" style="left:447px">
    <h2>EVISITOR<br><b>TOURIST ETA</b></h2>
    <p>Mit dem Visitor Visum können Touristen bis zu <b>drei Monaten</b> am Stück nach Australien reisen um dort Urlaub zu machen, Verwandte oder Bekannte zu besuchen. Eine arbeitsbezogene Nutzung dieses Visums ist ausdrücklich <b>nicht</b> gestattet!</p>
    <p class="note">Wichtig: Es muss bereits vor Antritt der Reise ein gültiges Visum vorliegen. Drucken Sie Ihre eVisitor Nummer aus und legen Sie diese Ihren Reisedokumenten bei.</p>
    <span class="btn">APPLICATION FORM</span>
  </article>
  <article class="card work" style="left:795px">
    <h2><b>WORK &amp;<br>TRAVEL</b></h2>
    <p>Geschäftsreisende benötigen ein Business eVisitor Visum. Dieses ebenso elektronisch erstellte Visum hat eine <b>Gültigkeit von 12 Monaten</b> und kann für einen durchgängigen Geschäftsaufenthalt für bis zu <b>drei Monaten</b> genutzt werden. Wir empfehlen auch bei Messebesuchen ein Business Visum zu beantragen um eine problemlose Einreise zu gewährleisten.</p>
    <p class="note">Wichtig: Es muss bereits vor Antritt der Reise ein gültiges Business Visum vorliegen. Drucken Sie Ihre eVisitor Nummer aus und legen Sie diese Ihren Reisedokumenten bei.</p>
    <span class="btn">APPLICATION FORM</span>
  </article>
</section>

<section class="faq">
  <h2>FAQ</h2>
  <p class="sub">Wir klären die wichtigsten Fragen</p>
  <div class="faq-q faq-first">Q: WELCHE DOKUMENTE ERHALTE ICH MIT MEINEM EVISITOR VISA?<span class="ico">–</span></div>
  <div class="faq-a">
    Sobald Ihre Evisitor Genehmigung erteilt worden ist erhalten Sie eine Bestätigung per Email. Dieses Dokument müssen Sie aufheben und mit Ihren Reisedokumenten zur Reise mitnehmen. Die Evisitor Dokumente umfassen
    <ul><li>Ihre eVisitor Genehmigungsnummer</li><li>Das Datum ab dem Ihre eVisitor Nummer gültig ist</li><li>Die allgemeinen eVisitor Konditionen und Bedingungen</li></ul>
    Mit einer gültigen eVisitornummer (ETA Visum) erhalten Sie bei der Einreise nach Australien keinen Eintrag, bzw. Stempel mehr in Ihren Reisepass. Die Crew Ihrer Airline übermittelt bereits während des Fluges Ihre Pass und eVisitor Daten an die Australischen Behörden.
  </div>
  <div class="faq-q">Q: WANN ERHALTE ICH MEINE EVISITOR ETA VISA GENEHMIGUNG?<span class="ico">+</span></div>
  <div class="faq-q">Q: WAS DARF MAN ALS EVISITOR (INHABER EINES ETA VISA) IN AUSTRALIEN MACHEN?<span class="ico">+</span></div>
</section>

<section class="tips">
  <div class="tips-photo" role="img" aria-label="Photo of the Sydney harbour skyline with opera house and bridge at dusk"></div>
  <h2>3 TIPPS</h2>
  <p class="sub">für eine erfolgreiche Australien Reise</p>
  <div class="tip" style="left:92px"><div class="num">1</div><h3>GÜLTIGE<br>REISEDOKUMENTE</h3><p>Gültige Reisedokumente für die gesamte Dauer des Aufenthaltes. Reisepass und vorläufiger Reisepass werden anerkannt. Kinder benötigen einen eigenen Reisepass. Personalausweis und vorläufiger Personalausweis sind nicht zugelassen. Sollten asiatische Staaten im Zuge der Reise besucht werden wollen, informieren Sie sich bitte über die speziellen Vorschriften, da manche Staaten eine Gültigkeit bis zu sechs Monaten ausländischer Reisepässe voraussetzen.</p></div>
  <div class="tip" style="left:449px"><div class="num">2</div><h3>EINHALTUNG<br>DER VORSCHRIFTEN</h3><p>Australien hat sehr strikte Einreise und Quarantänevorschriften. An etlichen Flughäfen ist mit Körperscannern bei der Einreise zu rechnen. Ebenso müssen eingeführte Nahrungsmittel, Tier- und Pflanzenprodukte auf der Einreisekarte angegeben werden. Striktes Befolgen der Anweisungen wird von uns empfohlen um unnötige Wartezeiten und Ärger zu vermeiden.</p></div>
  <div class="tip" style="left:806px"><div class="num">3</div><h3>EINHALTUNG<br>DER GESETZE</h3><p>Halten Sie sich an die Gesetze des Landes. Wie bereits erwähnt ist Australien ein liberales Land, solange die Gesetze befolgt werden. Illegale Aktivitäten wie Verstöße gegen die Visa Bestimmungen, die Ausfuhr von kulturellen Schätzen oder die Einnahme von illegalen Substanzen können zur Ausweisung bis hin zu Freiheitsstrafe in Australien führen.</p></div>
</section>

<section class="advantages">
  <h2>IHRE VORTEILE</h2>
  <p class="sub">mit visa-korvenet.org in der Übersicht</p>
  <table class="compare">
    <tr><th>UNSER SERVICE</th><th class="col-own">visa-korvenet.org</th><th class="col-gov">behoerden-portal.gov</th></tr>
    <tr><td>Anmeldeformular auf deutsch</td><td class="col-own">✓</td><td class="col-gov"></td></tr>
    <tr><td>Hilfe bei der Formulareingabe</td><td class="col-own">✓</td><td class="col-gov"></td></tr>
    <tr><td>Email Support</td><td class="col-own">✓</td><td class="col-gov"></td></tr>
    <tr><td>Auf Wunsch auch Sendung der ETA Nummer per Post</td><td class="col-own">✓</td><td class="col-gov"></td></tr>
    <tr><td>FAQ Section</td><td class="col-own">✓</td><td class="col-gov">✓</td></tr>
    <tr><td>Kontrolle Ihrer gemachten Eingaben</td><td class="col-own">✓</td><td class="col-gov">✓</td></tr>
    <tr><td>Rückmeldung und Überprüfung, ob Ihre Eingaben abgeschickt wurden</td><td class="col-own">✓</td><td class="col-gov">✓</td></tr>
    <tr><td>Manuelle Kontrolle bei Falscheingaben und Rückmeldung durch Supportmitarbeiter</td><td class="col-own">✓</td><td class="col-gov"></td></tr>
    <tr><td>Statusnachricht Ihres ETA-Antrages</td><td class="col-own">✓</td><td class="col-gov"></td></tr>
    <tr><td>ETA-Nummer Versand bequem per PDF</td><td class="col-own">✓</td><td class="col-gov"></td></tr>
    <tr><td>Aufbewahrung Ihrer ETA-Nummer für ein Jahr</td><td class="col-own">✓</td><td class="col-gov">✓</td></tr>
    <tr><td>Kostenlose Neuanforderung Ihrer ETA-Nummer innerhalb eines Jahres bei Verlust</td><td class="col-own">✓</td><td class="col-gov">✓</td></tr>
    <tr><td>Garantierte Rückerstattung der Gebühren, falls Ihre ETA Genehmigung zurückgewiesen wird</td><td class="col-own">✓</td><td class="col-gov"></td></tr>
  </table>
</section>

<section class="places">
  <div class="tile visit" role="img" aria-label="Photo of a turquoise coastline from above"><span>VISIT<br><b>THE<br>BEST<br>PLACES</b></span></div>
  <div class="tile sydney" role="img" aria-label="Photo of Sydney harbour"><span>EXPLORE<b>SYDNEY</b></span></div>
  <div class="tile perth" role="img" aria-label="Photo of the Perth skyline"><span>EXPLORE<b>PERTH</b></span></div>
  <div class="tile brisbane" role="img" aria-label="Photo of the Brisbane skyline"><span>EXPLORE<b>BRISBANE</b></span></div>
  <div class="tile melbourne" role="img" aria-label="Photo of the Melbourne skyline"><span>EXPLORE<b>MELBOURNE</b></span></div>
  <div class="tile tasmania" role="img" aria-label="Photo of red rocks on the Tasmanian coast"><span>EXPLORE<b>TASMANIA</b></span></div>
  <div class="tile goldcoast" role="img" aria-label="Photo of the Gold Coast beach and towers"><span>EXPLORE<b>GOLD COAST</b></span></div>
</section>

<footer class="site-footer">
  <div class="fcol contact">
    <h4>Contact information</h4>
    <p>We would be more than happy to help you. Our team advisor are from 10 am - 4 pm at your service to help you.</p>
    <div class="row"><svg width="16" height="12" viewBox="0 0 16 12"><rect x="0.5" y="0.5" width="15" height="11" fill="none" stroke="#ddd"/><path d="M1 1l7 6 7-6" fill="none" stroke="#ddd"/></svg><span>info@visa-korvenet.org</span></div>
    <div class="row"><svg width="16" height="16" viewBox="0 0 16 16"><path d="M3 1h3l1 4-2 1c1 2 3 4 5 5l1-2 4 1v3c0 1-1 2-2 2C7 15 1 9 1 3c0-1 1-2 2-2z" fill="#ddd"/></svg><span>Phone: 0800 100 200 300<br>Fax: &nbsp;&nbsp;089 100 200 400</span></div>
    <div class="row"><svg width="16" height="18" viewBox="0 0 16 18"><path d="M8 0a6 6 0 0 0-6 6c0 5 6 12 6 12s6-7 6-12a6 6 0 0 0-6-6zm0 8.5A2.5 2.5 0 1 1 8 3.5a2.5 2.5 0 0 1 0 5z" fill="#ddd"/></svg><span>Lindenweg 12<br>D-80331 Musterstadt</span></div>
  </div>
  <div class="fcol links">
    <h4>Useful links</h4>
    <a>GÜLTIGKEITSDAUER ETA-VISUM</a><a>ETA FORMULAR DEUTSCH</a><a>WAS IST ETA?</a><a>DATENSCHUTZ</a><a>AGB</a><a>IMPRESSUM</a>
  </div>
  <div class="fcol mailing">
    <h4>Mailing List</h4>
    <p>Enter your email address to our mailing list<br>to keep yourself updated.</p>
    <div class="mail-form"><span>Your email address</span><b>DONE</b></div>
    <h4 class="pay">Payment methods</h4>
    <div class="cards-row"><span>PayNow</span><span>CardOne</span><span>CardTwo</span></div>
  </div>
</footer>
<div class="copyright">Copyright 2017 © VISA KORVENET</div>

</body>
</html>
```